Business cards

We need business cards for the logo that you designed for our company. Something simple and clean.

Target Market(s)

Homeowners/ people looking for construction work

Industry/Entity Type

Construction

Contact Information for Business Card

Name: Doug Whitby, Number: 602-555-0174, Email: WhitbyBuildingCompany@mailbox-example.net ROC# 482063

Font styles to use
Serif

Colors

Designer to choose colors to be used in the design.

Requirements
Must have
• On one side of the card I would like to be all of the personal information I have put above along with the company logo that I have attached.
• On the other side of the card I would like the top half of the card to be the logo and then on the bottom half I would like to have the areas of construction we focus on along with an icon that represents it like the picture I have attached.
• Areas we focus on:
• Roofing, Kitchen and bath Remodel, Water Damage, Storm Damage, Fire Damage, Insurance Specialist
• If we could arrange those in alphabetical order.
Nice to have
• I have added 2 company logos a colorful one and a black one it would be nice to see a couple different options the black logo to be more simple and sleek and the colorful logo to be more colorful

```html
<!DOCTYPE html>
<html lang="en">
<head>
<meta charset="utf-8">
<title>Whitby Building Company — Business Cards</title>
<link rel="stylesheet" href="https://fonts.googleapis.com/css2?family=Rubik:wght@400;500;700&display=swap">
<style>
  :root {
    --stage: #d6d7d9;
    --card-white: #ffffff;
    --card-black: #141414;
    --brand-blue: #1e9cd7;
    --brand-red: #e0222e;
    --ink: #1b1b1b;
    --muted: #d8d8d8;
    --pin-green: #7db23a;
    --pin-ring: #e8efe0;
    --water: #2145a8;
    --fire: #c9322b;
    --mold: #5a8d34;
    --storm: #3a66b8;
    --commercial: #e08a2c;
  }
  * { box-sizing: border-box; margin: 0; padding: 0; }
  html, body { width: 1200px; height: 900px; overflow: hidden; }
  body {
    background: var(--stage);
    font-family: "Rubik", Arial, sans-serif;
    position: relative;
  }
  .card {
    position: absolute;
    left: 250px;
    width: 700px;
    height: 400px;
    border-radius: 18px;
    box-shadow: 0 10px 30px rgba(0,0,0,.25);
    overflow: hidden;
  }
  /* Front */
  .card--front { top: 40px; background: var(--card-white); }
  .brand {
    position: absolute;
    left: 50px;
    top: 160px;
    display: flex;
    align-items: center;
    gap: 14px;
  }
  .brand__mark { width: 30px; height: 30px; background: var(--brand-blue); flex: none; }
  .brand__name {
    font-weight: 700;
    font-size: 27px;
    letter-spacing: 1px;
    color: var(--brand-blue);
    text-transform: uppercase;
    line-height: 1.1;
  }
  .divider {
    position: absolute;
    left: 372px;
    top: 105px;
    width: 2px;
    height: 190px;
    background: var(--brand-blue);
  }
  .contact {
    position: absolute;
    left: 400px;
    top: 110px;
    color: var(--ink);
  }
  .contact__name {
    font-size: 34px;
    font-weight: 400;
    color: var(--brand-blue);
    text-transform: uppercase;
    letter-spacing: 1px;
  }
  .contact__role { font-size: 19px; margin-top: 2px; }
  .contact__roc { font-size: 18px; margin-top: 10px; }
  .contact__roc span { color: var(--brand-blue); }
  .contact__list { list-style: none; margin-top: 8px; font-size: 15px; }
  .contact__list li { display: flex; align-items: center; gap: 8px; margin-top: 5px; }
  .contact__list svg { width: 12px; height: 12px; flex: none; }
  /* Back */
  .card--back { top: 460px; background: var(--card-black); }
  .card--back .brand { top: 48px; left: 0; right: 0; justify-content: center; }
  .card--back .brand__mark { width: 40px; height: 40px; }
  .card--back .brand__name { font-size: 44px; }
  .services-line {
    position: absolute;
    top: 132px;
    left: 40px;
    right: 40px;
    text-align: center;
    color: var(--muted);
    font-size: 17px;
    letter-spacing: 1px;
    line-height: 1.5;
    text-transform: uppercase;
  }
  .services {
    position: absolute;
    top: 225px;
    left: 40px;
    right: 40px;
    display: flex;
    justify-content: space-between;
    list-style: none;
  }
  .service { width: 116px; text-align: center; color: #fff; }
  .service svg { width: 54px; height: 66px; display: block; margin: 0 auto 8px; }
  .service__title { font-weight: 700; font-size: 15px; text-transform: uppercase; }
  .service__sub { font-size: 11px; text-transform: uppercase; color: var(--muted); letter-spacing: .5px; }
  .service--active::after {
    content: "";
    display: block;
    width: 100px;
    height: 3px;
    margin: 8px auto 0;
    background: var(--pin-green);
  }
</style>
</head>
<body>

<section class="card card--front" aria-label="Business card front">
  <div class="brand">
    <span class="brand__mark"></span>
    <span class="brand__name">Whitby Building<br>Company</span>
  </div>
  <div class="divider"></div>
  <div class="contact">
    <h1 class="contact__name">Doug Whitby</h1>
    <p class="contact__role">Director</p>
    <p class="contact__roc"><span>ROC#</span> 482063</p>
    <ul class="contact__list">
      <li><svg viewBox="0 0 12 12"><path d="M3 1l2 2-1 1.5c.6 1.4 1.6 2.4 3 3L8.5 6.5l2 2-1.5 2C5 10 2 7 1.5 3z" fill="var(--brand-blue)"/></svg>602-555-0174</li>
      <li><svg viewBox="0 0 12 12"><rect x="1" y="2.5" width="10" height="7" fill="none" stroke="var(--brand-blue)"/><path d="M1 2.5l5 4 5-4" fill="none" stroke="var(--brand-blue)"/></svg>WhitbyBuildingCompany@mailbox-example.net</li>
      <li><svg viewBox="0 0 12 12"><circle cx="6" cy="6" r="5" fill="var(--brand-blue)"/></svg>www.WhitbyBuilding-example.com</li>
    </ul>
  </div>
</section>

<section class="card card--back" aria-label="Business card back">
  <div class="brand">
    <span class="brand__mark"></span>
    <span class="brand__name">Whitby Building Company</span>
  </div>
  <p class="services-line">Roofing - Kitchen and Bath Remodel - Water Damage<br>Storm Damage - Fire Damage - Insurance Specialist</p>
  <ul class="services">
    <li class="service">
      <svg viewBox="0 0 54 66"><path d="M27 64C12 46 3 36 3 26a24 24 0 0148 0c0 10-9 20-24 38z" fill="var(--pin-green)"/><circle cx="27" cy="26" r="17" fill="var(--pin-ring)"/><path d="M27 14c5 7 8 11 8 15a8 8 0 01-16 0c0-4 3-8 8-15z" fill="var(--water)"/></svg>
      <div class="service__title">Water</div><div class="service__sub">Damage</div>
    </li>
    <li class="service service--active">
      <svg viewBox="0 0 54 66"><path d="M27 64C12 46 3 36 3 26a24 24 0 0148 0c0 10-9 20-24 38z" fill="var(--pin-green)"/><circle cx="27" cy="26" r="17" fill="var(--pin-ring)"/><circle cx="27" cy="26" r="13" fill="var(--fire)"/></svg>
      <div class="service__title">Fire</div><div class="service__sub">Damage</div>
    </li>
    <li class="service">
      <svg viewBox="0 0 54 66"><path d="M27 64C12 46 3 36 3 26a24 24 0 0148 0c0 10-9 20-24 38z" fill="var(--pin-green)"/><circle cx="27" cy="26" r="17" fill="var(--pin-ring)"/><circle cx="27" cy="26" r="13" fill="var(--mold)"/></svg>
      <div class="service__title">Mold</div><div class="service__sub">Remediation</div>
    </li>
    <li class="service">
      <svg viewBox="0 0 54 66"><path d="M27 64C12 46 3 36 3 26a24 24 0 0148 0c0 10-9 20-24 38z" fill="var(--pin-green)"/><circle cx="27" cy="26" r="17" fill="var(--pin-ring)"/><circle cx="27" cy="26" r="13" fill="var(--storm)"/></svg>
      <div class="service__title">Storm</div><div class="service__sub">Damage</div>
    </li>
    <li class="service">
      <svg viewBox="0 0 54 66"><path d="M27 64C12 46 3 36 3 26a24 24 0 0148 0c0 10-9 20-24 38z" fill="var(--pin-green)"/><circle cx="27" cy="26" r="17" fill="var(--pin-ring)"/><circle cx="27" cy="26" r="13" fill="var(--commercial)"/></svg>
      <div class="service__title">Commercial</div><div class="service__sub">Services</div>
    </li>
  </ul>
</section>

</body>
</html>
```